New business card for civil engineering company - "Keystone Audit"

We need a business card designed for our new structural engineering company.

The company name is "Keystone Audit" logo files attached.

We would like the following:
* Two-sided card
* Simple design

Information to be placed on the card:
Name - Marcus Dellow
Job Title - Director / Structural Engineer
Credentials - BEng(Hons), CPEng, CMengNZ, IntPE(NZ)
Email - marcus.dellow@keystoneaudit.co.nz
mobile - 0219364058
website - www.keystoneaudit.co.nz

```html
<!DOCTYPE html>
<html lang="en">
<head>
<meta charset="utf-8">
<title>Keystone Audit – Business Card</title>
<link rel="stylesheet" href="https://fonts.googleapis.com/css2?family=Montserrat:wght@400;600&family=Open+Sans:wght@400&display=swap">
<style>
  :root {
    --page-bg: #f1f2f3;
    --card-white: #eceeef;
    --brand-blue: #1677c1;
    --blue-mid: #4b9ad6;
    --blue-light: #9cc8ea;
    --ink-dark: #3c4045;
    --ink-mid: #5d6369;
    --white: #ffffff;
  }
  * { box-sizing: border-box; margin: 0; padding: 0; }
  html, body {
    width: 1200px; height: 1000px; overflow: hidden;
    background: var(--page-bg);
    font-family: "Open Sans", Arial, sans-serif;
  }
  .canvas { position: relative; width: 1200px; height: 1000px; }
  .card {
    position: absolute; left: 220px; width: 760px; height: 434px;
    overflow: hidden; box-shadow: 0 6px 18px rgba(0,0,0,.12);
  }
  .card--front { top: 44px; background: var(--card-white); }
  .card--back { top: 522px; background: var(--brand-blue); }

  .wordmark {
    position: absolute; display: flex; align-items: center; gap: 10px;
    font-family: "Montserrat", Arial, sans-serif; font-weight: 600;
    letter-spacing: 1px; text-transform: uppercase; white-space: nowrap;
  }
  .wordmark__square { display: block; flex: none; }
  .card--front .wordmark { left: 70px; top: 78px; font-size: 24px; color: var(--ink-dark); }
  .card--front .wordmark .wordmark__square { width: 16px; height: 16px; background: var(--brand-blue); }

  .contact-list { position: absolute; left: 70px; top: 140px; list-style: none; }
  .contact-list li {
    display: flex; align-items: center; gap: 10px;
    font-size: 13px; color: var(--ink-mid); line-height: 22px;
  }
  .contact-list svg { width: 12px; height: 12px; fill: var(--brand-blue); flex: none; }

  .person { position: absolute; right: 62px; top: 170px; text-align: right; }
  .person__name {
    font-family: "Montserrat", Arial, sans-serif; font-weight: 400;
    font-size: 26px; letter-spacing: 1px; text-transform: uppercase; color: var(--brand-blue);
  }
  .person__name .surname { color: var(--ink-dark); }
  .person__title { font-size: 15px; color: var(--ink-mid); margin-top: 2px; }
  .person__credentials { font-size: 10px; color: var(--ink-mid); margin-top: 3px; }

  .front-band { position: absolute; left: 0; top: 0; width: 760px; height: 434px; }

  .card--front .wordmark--small {
    left: auto; right: 28px; top: auto; bottom: 22px;
    font-size: 12px; color: var(--white); gap: 6px;
  }
  .card--front .wordmark--small .wordmark__square { width: 9px; height: 9px; background: var(--white); }

  .card--back .wordmark {
    left: 50%; top: 50%; transform: translate(-50%, -50%);
    font-size: 34px; color: var(--white); gap: 14px;
  }
  .card--back .wordmark .wordmark__square { width: 22px; height: 22px; background: var(--white); }
</style>
</head>
<body>
<main class="canvas">
  <section class="card card--front" aria-label="Business card front">
    <svg class="front-band" viewBox="0 0 760 434" aria-hidden="true">
      <polygon points="0,262 760,372 760,396 0,300" fill="var(--blue-light)"/>
      <polygon points="0,282 760,384 760,410 0,316" fill="var(--blue-mid)"/>
      <polygon points="0,300 760,396 760,434 0,434" fill="var(--brand-blue)"/>
    </svg>

    <div class="wordmark"><span class="wordmark__square"></span>Keystone Audit</div>

    <ul class="contact-list">
      <li>
        <svg viewBox="0 0 24 24"><path d="M6.6 10.8a15 15 0 0 0 6.6 6.6l2.2-2.2a1 1 0 0 1 1-.25 11.4 11.4 0 0 0 3.6.57 1 1 0 0 1 1 1V20a1 1 0 0 1-1 1A17 17 0 0 1 3 4a1 1 0 0 1 1-1h3.5a1 1 0 0 1 1 1c0 1.25.2 2.45.57 3.6a1 1 0 0 1-.25 1z"/></svg>
        0219364058
      </li>
      <li>
        <svg viewBox="0 0 24 24"><path d="M2 5h20v14H2z M2 5l10 8 10-8" fill="none" stroke="var(--brand-blue)" stroke-width="2.4"/></svg>
        marcus.dellow@keystoneaudit.co.nz
      </li>
      <li>
        <svg viewBox="0 0 24 24"><circle cx="12" cy="12" r="9.5" fill="none" stroke="var(--brand-blue)" stroke-width="2.4"/><path d="M2.5 12h19M12 2.5c3 3 3 16 0 19M12 2.5c-3 3-3 16 0 19" fill="none" stroke="var(--brand-blue)" stroke-width="2"/></svg>
        www.keystoneaudit.co.nz
      </li>
    </ul>

    <div class="person">
      <h1 class="person__name">Marcus <span class="surname">Dellow</span></h1>
      <p class="person__title">Structural Engineer</p>
      <p class="person__credentials">BEng(Hons), CPEng, CMEngNZ, IntPE(NZ)</p>
    </div>

    <div class="wordmark wordmark--small"><span class="wordmark__square"></span>Keystone Audit</div>
  </section>

  <section class="card card--back" aria-label="Business card back">
    <div class="wordmark"><span class="wordmark__square"></span>Keystone Audit</div>
  </section>
</main>
</body>
</html>
```